Calibrated NET Systems
Business card and Stationary
Project: Calibrated NET Systems
Calibrated NET Systems - Information Technology
Creative Brief
Professional
Dean Harlowe
Technical Consultant
Please leave the address part blank.
dean.harlowe@calnet.ca
www.calnet.ca

```html
<!DOCTYPE html>
<html lang="en">
<head>
<meta charset="utf-8">
<title>Calibrated NET Systems – Business Card</title>
<link href="https://fonts.googleapis.com/css2?family=Arimo:wght@400;700&display=swap" rel="stylesheet">
<style>
  :root {
    --page-bg: #e9ecef;
    --card-bg: #ffffff;
    --sky: #6fd0f4;
    --azure: #2aa6dd;
    --navy: #0f4f8a;
    --deep-navy: #0b3764;
    --swoosh-grey: #c9ccd0;
    --brand-blue: #2a8fc8;
    --text-dark: #2b2f33;
    --icon-blue: #1f6fa8;
    --badge-grey: #dfe3e8;
  }
  * { margin: 0; padding: 0; box-sizing: border-box; }
  html, body {
    width: 1200px; height: 778px; overflow: hidden;
    background: var(--page-bg);
    font-family: "Arimo", Arial, sans-serif;
  }
  .business-card {
    position: absolute; left: 80px; top: 87px;
    width: 1040px; height: 604px;
    background: var(--card-bg);
    border-radius: 26px;
    overflow: hidden;
    box-shadow: 0 4px 14px rgba(0,0,0,0.15);
  }
  .card-art { position: absolute; inset: 0; }
  .holder {
    position: absolute; right: 58px; top: 40px;
    text-align: right; color: #fff;
  }
  .holder-name { font-size: 32px; font-weight: 700; line-height: 1.2; }
  .holder-title { font-size: 23px; font-weight: 700; margin-top: 8px; }
  .brand {
    position: absolute; left: 78px; top: 205px;
    display: flex; align-items: center; gap: 26px;
  }
  .brand-mark {
    width: 110px; height: 110px;
    background: var(--azure);
    border-radius: 6px;
  }
  .brand-name {
    font-size: 46px; font-weight: 400; color: var(--brand-blue);
    letter-spacing: 0.5px;
  }
  .contact-list {
    position: absolute; left: 84px; top: 432px;
    list-style: none;
  }
  .contact-item {
    display: flex; align-items: center; gap: 18px;
    font-size: 23px; color: var(--text-dark);
    height: 34px;
  }
  .contact-icon { width: 20px; height: 20px; fill: var(--icon-blue); flex: none; }
  .cert-badge {
    position: absolute; right: 78px; bottom: 52px;
    width: 200px; height: 96px;
    background: var(--badge-grey);
    border-radius: 8px;
  }
</style>
</head>
<body>
  <div class="business-card">
    <svg class="card-art" viewBox="0 0 1040 604" width="1040" height="604" aria-hidden="true">
      <defs>
        <linearGradient id="band-gradient" x1="0" y1="0" x2="1" y2="0">
          <stop offset="0" stop-color="var(--sky)"/>
          <stop offset="0.45" stop-color="var(--azure)"/>
          <stop offset="0.6" stop-color="var(--navy)"/>
          <stop offset="1" stop-color="var(--deep-navy)"/>
        </linearGradient>
      </defs>
      <path class="swoosh-shadow" d="M300,140 C600,150 880,220 1040,370 V300 C870,180 600,140 300,140 Z" fill="var(--swoosh-grey)"/>
      <path class="top-band" d="M0,0 H1040 V330 C860,170 560,105 0,90 Z" fill="url(#band-gradient)"/>
      <path class="swoosh-line" d="M170,155 C520,150 860,230 1040,400" fill="none" stroke="var(--swoosh-grey)" stroke-width="3"/>
    </svg>

    <div class="holder">
      <p class="holder-name">Dean Harlowe</p>
      <p class="holder-title">Technical Consultant</p>
    </div>

    <div class="brand">
      <div class="brand-mark"></div>
      <p class="brand-name">Calibrated NET Systems</p>
    </div>

    <ul class="contact-list">
      <li class="contact-item">
        <svg class="contact-icon" viewBox="0 0 20 20"><path d="M10 2 L19 10 H16 V18 H12 V13 H8 V18 H4 V10 H1 Z"/></svg>
        1-555-010-4821
      </li>
      <li class="contact-item">
        <svg class="contact-icon" viewBox="0 0 20 20"><path d="M5 2 C3 2 2 4 2 6 C3 12 8 17 14 18 C16 18 18 17 18 15 L15 12 L12 14 C9 13 7 11 6 8 L8 5 Z"/></svg>
        1-555-010-7369
      </li>
      <li class="contact-item">
        <svg class="contact-icon" viewBox="0 0 20 20"><path d="M2 4 H18 V16 H2 Z M3 5 L10 11 L17 5" fill="none" stroke="var(--icon-blue)" stroke-width="1.8"/></svg>
        dean.harlowe@calnet.ca
      </li>
      <li class="contact-item">
        <svg class="contact-icon" viewBox="0 0 20 20"><circle cx="10" cy="10" r="8" fill="none" stroke="var(--icon-blue)" stroke-width="1.8"/><path d="M2 10 H18 M10 2 C6 6 6 14 10 18 M10 2 C14 6 14 14 10 18" fill="none" stroke="var(--icon-blue)" stroke-width="1.4"/></svg>
        www.calnet.ca
      </li>
    </ul>

    <div class="cert-badge" role="img" aria-label="Professional certification badge"></div>
  </div>
</body>
</html>
```